PPT Template for an investment fund to use in their pitchbooks

Our firm is an international investment fund and are seeking a PPT template to use in our pitch book (and subsequent PPTs). We would need a template for a title slide and then subsequent text/info slides. A clean & uncluttered feel is preferred as well as no watermark on slides. Please see our logo attached. The logo color code is #19478d. Font is Gotham-Medium.

Target Market(s)

Sophisticated investors

Industry/Entity Type

Finance

Colors
ffffff
0356a4

```html
<!DOCTYPE html>
<html lang="en">
<head>
<meta charset="UTF-8">
<title>Pitchbook Title Slide</title>
<link href="https://fonts.googleapis.com/css2?family=Montserrat:wght@500;600&display=swap" rel="stylesheet">
<style>
  :root {
    --brand-navy: #19478d;
    --brand-blue: #0356a4;
    --card-blue: #0668c2;
    --card-shadow: #142f5e;
    --band-light: #3d6fc4;
    --white: #ffffff;
  }
  html, body {
    margin: 0;
    padding: 0;
    width: 1200px;
    height: 675px;
    overflow: hidden;
    background: var(--white);
  }
  .slide {
    position: relative;
    width: 1200px;
    height: 675px;
    overflow: hidden;
    font-family: "Montserrat", Arial, sans-serif;
    color: var(--white);
  }
  .team-photo {
    position: absolute;
    inset: 0 0 auto 0;
    height: 460px;
    background:
      radial-gradient(ellipse at 78% 40%, rgba(120, 72, 40, 0.55), transparent 55%),
      linear-gradient(100deg, #5f5d5c 0%, #7c7873 35%, #8b8580 55%, #6e4f38 75%, #5a4f4a 100%);
    filter: brightness(0.8);
  }
  .shapes {
    position: absolute;
    inset: 0;
  }
  .title-box {
    position: absolute;
    left: 464px;
    top: 15px;
    width: 272px;
    height: 97px;
    background: rgba(3, 86, 164, 0.82);
    display: flex;
    align-items: center;
    justify-content: center;
  }
  .title-box h1 {
    margin: 0;
    font-weight: 600;
    font-size: 64px;
    letter-spacing: 2px;
    line-height: 1;
  }
  .card-label {
    position: absolute;
    margin: 0;
    font-weight: 600;
    font-size: 28px;
    letter-spacing: 0.3px;
    transform: translateX(-50%);
    white-space: nowrap;
  }
  .label-innovation { left: 239px; top: 382px; }
  .label-eco { left: 616px; top: 357px; }
  .label-profit { left: 975px; top: 363px; }
  .dollar-sign {
    position: absolute;
    left: 962px;
    top: 408px;
    transform: translateX(-50%);
    font-weight: 600;
    font-size: 92px;
    line-height: 1;
  }
  .brand-name {
    position: absolute;
    right: 20px;
    bottom: 28px;
    display: flex;
    align-items: center;
    gap: 8px;
    font-weight: 600;
    font-size: 13px;
    letter-spacing: 0.6px;
  }
  .brand-square {
    width: 10px;
    height: 10px;
    background: var(--white);
  }
</style>
</head>
<body>
<main class="slide">
  <div class="team-photo" role="img" aria-label="Photo of a small team of colleagues smiling and working together at a table"></div>

  <svg class="shapes" width="1200" height="675" viewBox="0 0 1200 675" aria-hidden="true">
    <polygon points="0,447 1200,422 1200,675 0,675" fill="var(--brand-navy)"/>
    <polygon points="0,447 420,439 420,450 0,475" fill="var(--band-light)" opacity="0.6"/>

    <polygon points="123,378 384,361 341,542 83,556" fill="var(--card-shadow)"/>
    <polygon points="114,370 374,353 331,534 73,547" fill="var(--card-blue)"/>

    <polygon points="503,355 759,336 718,519 459,530" fill="var(--card-shadow)"/>
    <polygon points="494,347 749,328 708,511 449,522" fill="var(--card-blue)"/>

    <polygon points="862,360 1121,342 1082,522 822,535" fill="var(--card-shadow)"/>
    <polygon points="853,352 1111,334 1072,514 812,527" fill="var(--card-blue)"/>

    <g class="icon-bulb" fill="var(--white)">
      <path d="M223,426 a31,31 0 0 1 19,55 v11 h-38 v-11 a31,31 0 0 1 19,-55 z"/>
      <rect x="210" y="496" width="27" height="12" rx="4"/>
      <path d="M233,438 a20,20 0 0 1 10,14" stroke="var(--card-blue)" stroke-width="4" fill="none" stroke-linecap="round"/>
    </g>

    <g class="icon-leaf">
      <path d="M560,494 C556,448 592,424 638,421 C636,466 612,496 568,490 Z" fill="var(--white)"/>
      <path d="M562,497 C580,470 600,450 626,432" stroke="var(--card-blue)" stroke-width="3" fill="none" stroke-linecap="round"/>
      <path d="M560,499 L568,488" stroke="var(--white)" stroke-width="3" stroke-linecap="round"/>
    </g>
  </svg>

  <div class="title-box"><h1>TITLE</h1></div>

  <p class="card-label label-innovation">INNOVATION</p>
  <p class="card-label label-eco">ECO-FRIENDLY</p>
  <p class="card-label label-profit">PROFITABLE</p>
  <span class="dollar-sign">$</span>

  <div class="brand-name"><span class="brand-square"></span><span>BASTION CLAIM CAPITAL</span></div>
</main>
</body>
</html>
```